Email Notification & Marketing Templates

I want to start with something like a newsletter or informational email, but i need Top Tips to Detect Phishing Scams. Something that i can send to users so they can follow it when receiving or exchanging emails. I will also need promotional items for my company that i can send to customers as well. It can be based on on our website QRVLINK.COM

Will also need:
newsletters
announcements
marketing emails
alerts
security notifications

Examples:Items such as Security Awareness Poster Series
Phishing Awareness
Password Security
Email Attachments
QR Code scams
Public WiFi safety

```html
<!DOCTYPE html>
<html lang="en">
<head>
<meta charset="utf-8">
<title>Top Tips to Detect Phishing Scams – QRV Link Networks</title>
<link rel="stylesheet" href="https://fonts.googleapis.com/css2?family=Montserrat:wght@700;800&family=Lexend:wght@400;600&display=swap">
<style>
  :root {
    --green: #4fae1f;
    --green-dark: #2f8a17;
    --green-light: #8fd14f;
    --ink: #111111;
    --text: #1d1d1d;
    --header-bg: #e6e6e6;
    --card-bg: #e8e8e8;
    --page-bg: #ffffff;
    --warn-red: #e0403a;
    --warn-orange: #f08a3a;
    --warn-pink: #f2a6a0;
    --muted: #9a9a9a;
  }
  * { box-sizing: border-box; margin: 0; padding: 0; }
  html, body { width: 670px; height: 1200px; overflow: hidden; background: var(--page-bg); }
  .poster {
    position: relative; width: 670px; height: 1200px; overflow: hidden;
    background: var(--page-bg); font-family: "Lexend", Arial, sans-serif; color: var(--text);
  }

  /* Header */
  .masthead { position: absolute; left: 0; top: 0; width: 670px; height: 161px; background: var(--header-bg); }
  .brand { position: absolute; left: 52px; top: 62px; display: flex; align-items: center; gap: 12px; }
  .brand-square { width: 30px; height: 30px; background: var(--ink); }
  .brand-name {
    font-family: "Lexend", Arial, sans-serif; font-weight: 600; font-size: 30px;
    line-height: 36px; color: var(--ink);
  }
  .hero-icon {
    position: absolute; left: 452px; top: 22px; width: 168px; height: 118px; border-radius: 18px;
    background: linear-gradient(135deg, var(--green-light), var(--green-dark));
  }

  /* Title */
  .title {
    position: absolute; left: 0; top: 184px; width: 670px; text-align: center;
    font-family: "Montserrat", Arial, sans-serif; font-weight: 800; font-size: 47px;
    line-height: 52px; color: var(--ink);
  }

  .warn { position: absolute; }

  /* Tips */
  .tips { position: absolute; left: 52px; top: 312px; width: 566px; list-style: none; }
  .tip {
    position: relative; height: 105px; margin-bottom: 12px; background: var(--card-bg);
    border-radius: 8px;
  }
  .tip-icon {
    position: absolute; left: 24px; top: 50%; transform: translateY(-50%);
    width: 70px; height: 70px; border-radius: 12px;
  }
  .tip-body { position: absolute; left: 129px; right: 8px; top: 50%; transform: translateY(-50%); }
  .tip-title { font-weight: 600; font-size: 18.5px; line-height: 25px; color: var(--ink); }
  .tip-text { font-size: 17.5px; line-height: 25px; color: var(--text); }

  .icon-hacker { background: linear-gradient(135deg, #6b6b6b, #2f2f2f); }
  .icon-urgency { background: linear-gradient(135deg, #f2c79a, #7a7a7a); }
  .icon-link { background: linear-gradient(135deg, #6fc24a, #3b7fc8); }
  .icon-person { background: linear-gradient(135deg, #f4f4f4, #bdbdbd); }
  .icon-safe { background: linear-gradient(135deg, #9a9a9a, #4d4d4d); }
  .icon-file { background: linear-gradient(135deg, #f6f6f6, #d9534f); }

  /* Floating "fake email" cards */
  .fake-email {
    position: absolute; width: 104px; height: 76px; background: #f5f5f5;
    border: 1px solid #dcdcdc; border-radius: 5px; opacity: 0.85;
    box-shadow: 0 2px 6px rgba(0,0,0,0.08);
  }
  .fake-email .bar { height: 11px; border-bottom: 1px solid #e0e0e0; display: flex; gap: 3px; padding: 3px 5px; }
  .fake-email .dot { width: 4px; height: 4px; border-radius: 50%; background: #c8c8c8; }
  .fake-email .dot:first-child { background: #7cc35a; }
  .fake-email .label { font-size: 15px; color: var(--muted); padding: 6px 0 0 8px; line-height: 18px; }
  .fake-email .line { height: 2px; background: #dedede; margin: 5px 8px 0; }
  .fake-email .line.short { width: 50%; }

  /* Call to action */
  .cta {
    position: absolute; left: 204px; top: 1025px; width: 262px; height: 50px;
    background: var(--green); border-radius: 7px; color: #fff; text-align: center;
    font-family: "Montserrat", Arial, sans-serif; font-weight: 700; font-size: 21px;
    line-height: 50px; letter-spacing: 0.5px;
  }

  /* Footer */
  .footer {
    position: absolute; left: 0; top: 1150px; width: 670px; text-align: center;
    font-size: 12px; line-height: 17px; color: var(--ink);
  }
</style>
</head>
<body>
<svg width="0" height="0" style="position:absolute" aria-hidden="true">
  <defs>
    <symbol id="warn-tri" viewBox="0 0 32 28">
      <path d="M16 2 L30 26 H2 Z" fill="currentColor" stroke="currentColor" stroke-width="2" stroke-linejoin="round"/>
      <rect x="14.6" y="9" width="2.8" height="9" rx="1.2" fill="#fff"/>
      <circle cx="16" cy="21.5" r="1.6" fill="#fff"/>
    </symbol>
  </defs>
</svg>

<main class="poster">
  <header class="masthead">
    <div class="brand">
      <span class="brand-square"></span>
      <span class="brand-name">QRV Link Networks</span>
    </div>
    <div class="hero-icon" role="img" aria-label="Green security shield beside an email envelope"></div>
  </header>

  <h1 class="title">TOP TIPS TO DETECT<br>PHISHING SCAMS</h1>

  <svg class="warn" style="left:610px;top:184px;color:var(--warn-red)" width="34" height="30"><use href="#warn-tri"/></svg>
  <svg class="warn" style="left:603px;top:226px;color:var(--warn-orange)" width="22" height="19"><use href="#warn-tri"/></svg>
  <svg class="warn" style="left:34px;top:218px;color:var(--warn-red)" width="22" height="19"><use href="#warn-tri"/></svg>
  <svg class="warn" style="left:22px;top:248px;color:var(--warn-pink)" width="20" height="17"><use href="#warn-tri"/></svg>
  <svg class="warn" style="left:44px;top:262px;color:var(--warn-orange)" width="28" height="24"><use href="#warn-tri"/></svg>

  <ol class="tips">
    <li class="tip">
      <div class="tip-icon icon-hacker" role="img" aria-label="Hooded hacker holding an envelope"></div>
      <div class="tip-body">
        <p class="tip-title">1. Inspect the Sender’s Email Address.</p>
        <p class="tip-text">Look for minor spelling errors or odd<br>domain names.</p>
      </div>
    </li>
    <li class="tip">
      <div class="tip-icon icon-urgency" role="img" aria-label="Clock beside a stressed person"></div>
      <div class="tip-body">
        <p class="tip-title">2. Beware of High-Pressure Tactics.</p>
        <p class="tip-text">Scammers create a false sense of urgency<br>(e.g., “Act now or lose access”).</p>
      </div>
    </li>
    <li class="tip">
      <div class="tip-icon icon-link" role="img" aria-label="Broken chain link with warning mark"></div>
      <div class="tip-body">
        <p class="tip-title">3. Check Links Before Clicking.</p>
        <p class="tip-text">Hover your mouse to see the real URL.<br>Is it different?</p>
      </div>
    </li>
    <li class="tip">
      <div class="tip-icon icon-person" role="img" aria-label="Generic user silhouette"></div>
      <div class="tip-body">
        <p class="tip-title">4. Watch for Generic Greetings.</p>
        <p class="tip-text">Phishing emails often use 'Dear Customer'<br>instead of your name.</p>
      </div>
    </li>
    <li class="tip">
      <div class="tip-icon icon-safe" role="img" aria-label="Locked safe with question mark"></div>
      <div class="tip-body">
        <p class="tip-title">5. Be Suspicious of Requests for<br>Sensitive Info.</p>
        <p class="tip-text">QRV will never ask for your password via email.</p>
      </div>
    </li>
    <li class="tip">
      <div class="tip-icon icon-file" role="img" aria-label="Document with red cross mark"></div>
      <div class="tip-body">
        <p class="tip-title">6. Don’t Open Unexpected Attachments.</p>
        <p class="tip-text">Malicious files can contain malware.</p>
      </div>
    </li>
  </ol>

  <div class="fake-email" style="left:568px;top:381px">
    <div class="bar"><span class="dot"></span><span class="dot"></span><span class="dot"></span></div>
    <p class="label">fake email</p><div class="line"></div><div class="line short"></div>
  </div>
  <svg class="warn" style="left:537px;top:395px;color:var(--warn-red)" width="18" height="16"><use href="#warn-tri"/></svg>
  <svg class="warn" style="left:652px;top:368px;color:var(--warn-pink)" width="24" height="21"><use href="#warn-tri"/></svg>

  <div class="fake-email" style="left:555px;top:616px">
    <div class="bar"><span class="dot"></span><span class="dot"></span><span class="dot"></span></div>
    <p class="label">fake email</p><div class="line"></div><div class="line short"></div>
  </div>
  <svg class="warn" style="left:524px;top:630px;color:var(--warn-red)" width="18" height="16"><use href="#warn-tri"/></svg>
  <svg class="warn" style="left:643px;top:602px;color:var(--warn-red)" width="26" height="23"><use href="#warn-tri"/></svg>

  <div class="fake-email" style="left:-4px;top:863px">
    <div class="bar"><span class="dot"></span><span class="dot"></span><span class="dot"></span></div>
    <p class="label">fake email</p><div class="line"></div><div class="line short"></div>
  </div>
  <svg class="warn" style="left:88px;top:856px;color:var(--warn-pink)" width="24" height="21"><use href="#warn-tri"/></svg>

  <div class="cta">STAY PROTECTED</div>

  <footer class="footer">
    <p>QRV Link Networks - (555) 010-4821 or (555) 010-7394</p>
    <p>Unsubscribe info@qrvlink.com</p>
  </footer>
</main>
</body>
</html>
```